Inflatable Movie Screen company needs a Brochure Design for sales kit

We need a brochure as per attached sketch drawing which is to:
1)follow the sample layout
2) attached images must be used
3) to follow company corporate colors or suggest something professional and appropriate for the theme
Updates

Target Market(s)

Corporate and Community Clubs

Industry/Entity Type

Entertainment

Requirements
Must have
• Colors to be in line with corporate colors OR to suggest something appropriate.
Nice to have
• A unique concept
Should not have
• Too fanciful

```html
<!DOCTYPE html>
<html lang="en">
<head>
<meta charset="utf-8">
<title>Inflatable Movie Screening Brochure</title>
<link href="https://fonts.googleapis.com/css2?family=Cinzel:wght@400;500&family=Poppins:ital,wght@0,300;0,400;0,600;1,300&display=swap" rel="stylesheet">
<style>
  :root {
    --stage: #dcdcdc;
    --paper: #ffffff;
    --navy: #0d2a45;
    --navy-light: #1f5f80;
    --grey: #8b8b8e;
    --grey-band: rgba(135,135,138,0.92);
    --teal: #14bec4;
    --bar: #2f4858;
    --ink: #2a2a2a;
    --white: #ffffff;
  }
  * { margin: 0; padding: 0; box-sizing: border-box; }
  html, body { width: 1200px; height: 901px; overflow: hidden; background: var(--stage); }
  .brochure {
    position: absolute; left: 300px; top: 26px;
    width: 600px; height: 848px;
    background: var(--paper); overflow: hidden;
    box-shadow: 0 6px 24px rgba(0,0,0,0.15);
  }
  .artwork { position: absolute; inset: 0; width: 600px; height: 848px; }
  .headline {
    position: absolute; left: 42px; top: 62px;
    font-family: 'Cinzel', serif; color: var(--white); line-height: 1;
  }
  .headline .line-small { font-size: 30px; display: block; letter-spacing: 1px; }
  .headline .line-big { font-size: 96px; display: block; margin: 2px 0 0 -4px; letter-spacing: -1px; }
  .headline .line-mid { font-size: 40px; display: block; margin: 2px 0 0 48px; letter-spacing: -1px; }
  .headline .line-mid small { font-size: 26px; }
  .brand {
    position: absolute; left: 350px; top: 192px; width: 240px;
    font-family: 'Cinzel', serif; color: var(--white); text-align: center;
  }
  .brand .brand-name { font-size: 52px; line-height: 1; display: flex; align-items: center; justify-content: center; gap: 10px; }
  .brand .brand-mark { width: 12px; height: 12px; border-radius: 50%; background: var(--white); display: inline-block; }
  .brand .brand-sub { font-size: 9px; letter-spacing: 1px; margin-top: 6px; display: block; }
  .testimonial {
    position: absolute; left: 50px; top: 640px; width: 250px;
    font-family: 'Poppins', sans-serif; font-size: 13.5px; color: var(--ink); line-height: 1.55;
  }
  .quote-mark { font-family: Georgia, serif; font-size: 54px; color: #777; line-height: 0.6; display: block; }
  .quote-mark.close { text-align: right; margin-top: -14px; margin-right: 20px; }
  .testimonial cite { font-style: normal; font-weight: 600; display: block; margin-top: 6px; }
  .website {
    position: absolute; left: 50px; top: 790px;
    font-family: 'Poppins', sans-serif; font-size: 9px; letter-spacing: 2px; color: #555; font-weight: 600;
  }
  .saying {
    position: absolute; left: 360px; top: 700px; width: 200px;
    font-family: 'Poppins', sans-serif; font-size: 13.5px; color: var(--ink); line-height: 1.65; text-align: center;
  }
  .saying cite { font-style: normal; font-weight: 600; display: block; margin-top: 18px; text-align: right; padding-right: 14px; }
  .footer-bar { position: absolute; left: 370px; top: 818px; width: 218px; height: 14px; background: var(--bar); }
</style>
</head>
<body>
<main class="brochure">
  <svg class="artwork" viewBox="0 0 600 848" xmlns="http://www.w3.org/2000/svg">
    <defs>
      <linearGradient id="navyGrad" x1="0" y1="0" x2="1" y2="1">
        <stop offset="0" stop-color="#0b2440"/>
        <stop offset="0.6" stop-color="#15476a"/>
        <stop offset="1" stop-color="#0d2a45"/>
      </linearGradient>
      <linearGradient id="eventGrad" x1="0" y1="0" x2="0" y2="1">
        <stop offset="0" stop-color="#cfd8e6"/>
        <stop offset="0.35" stop-color="#7d8aa0"/>
        <stop offset="0.6" stop-color="#5d6a55"/>
        <stop offset="1" stop-color="#4f6d3e"/>
      </linearGradient>
      <linearGradient id="nightGrad" x1="0" y1="0" x2="0" y2="1">
        <stop offset="0" stop-color="#1c2e3c"/>
        <stop offset="0.5" stop-color="#34503e"/>
        <stop offset="1" stop-color="#2c4a2e"/>
      </linearGradient>
      <clipPath id="pageClip"><rect width="600" height="848"/></clipPath>
    </defs>
    <g clip-path="url(#pageClip)">
      <path class="navy-facets" d="M0 0 H240 Q90 200 120 420 Q140 520 60 590 L0 600 Z" fill="url(#navyGrad)"/>
      <circle class="ring-teal" cx="390" cy="350" r="320" fill="none" stroke="var(--teal)" stroke-width="34"
              stroke-dasharray="380 2100" stroke-dashoffset="-760"/>
      <circle class="ring-grey" cx="390" cy="350" r="290" fill="none" stroke="var(--grey)" stroke-width="44"/>
      <circle cx="390" cy="350" r="268" fill="url(#eventGrad)" role="img"
              aria-label="Photo of an outdoor crowd seated on a lawn watching an inflatable movie screen at dusk"/>
      <rect class="header-band" x="12" y="40" width="338" height="248" fill="var(--grey-band)"/>
      <rect class="brand-band" x="340" y="176" width="260" height="96" fill="var(--grey-band)"/>
      <circle cx="142" cy="500" r="84" fill="var(--teal)"/>
      <circle cx="142" cy="500" r="74" fill="url(#nightGrad)" role="img"
              aria-label="Photo of an evening outdoor movie screening with audience on the grass"/>
    </g>
  </svg>

  <h1 class="headline">
    <span class="line-small">Inflatable</span>
    <span class="line-big">MOVIE</span>
    <span class="line-mid">SCREENING<small>BY</small></span>
  </h1>

  <div class="brand">
    <span class="brand-name"><span class="brand-mark"></span>LUMORA</span>
    <span class="brand-sub">LUMORA EVENTS PTE LTD</span>
  </div>

  <blockquote class="testimonial">
    <span class="quote-mark">&ldquo;</span>
    Enjoyed watching movie name 7 with my family. It was nice to get away from the usual malls and bond together. My kids loved it!
    <cite>-May Tan, Housewife</cite>
    <span class="quote-mark close">&rdquo;</span>
  </blockquote>

  <p class="website">WWW.LUMORAEVENTS.COM</p>

  <blockquote class="saying">
    "Of all our inventions for mass communications, pictures still speak the most universally understood language."
    <cite>- Arthur Penwell</cite>
  </blockquote>

  <div class="footer-bar"></div>
</main>
</body>
</html>
```